CalmHaven Webpage for Integrative and Holistic Psychiatric Practice

We need a webpage designed for a medical practice that focuses on integrative and holistic psychiatry. We focus on providing care to mothers and families. The name of the company is Calm Haven, incorporated, A Professional Medical Corporation.

We'd like the color palette to be earthy/natural with the same look and feel as our logo that's attached. We're not set on anything, so feel free to have fun with the palette. We just want it to be warm and inviting in particular for Moms!

We'd like to have our logo in the top left with links below it either centered or to the right. We really like websites like http://www.brightmeadowclinic.example/home.html and http://www.tarnwickmindpartners.example/site/ to give you an idea of what we're looking for.

For links, we're looking for the following. Dummy text is fine, we're still getting content together:

* Home
* About Us - this page would have headings for Directions, Staff, Appointment Scheduling
* Services Provided - headings for 8 different services
* Patient Resources - headings for Patient Forms, Fees, Articles
* FAQ
* Contact Us

The webpage will be hosted as an Office 365 Public Website, so feel free to use whatever SharePoint integration you would like, but it's not necessary.

Thank you!

```html
<!DOCTYPE html>
<html lang="en">
<head>
<meta charset="utf-8">
<title>CalmHaven — Holistic Psychiatry</title>
<link href="https://fonts.googleapis.com/css2?family=Questrial&display=swap" rel="stylesheet">
<style>
  :root {
    --brown: #7a3300;
    --nav-brown: #7a3a0a;
    --green: #1d6b0c;
    --btn-top: #2a9a1c;
    --btn-bottom: #137209;
    --body-text: #4a4a4a;
    --white: #ffffff;
    --band: rgba(120, 175, 110, 0.55);
  }
  * { margin: 0; padding: 0; box-sizing: border-box; }
  html, body { width: 1075px; height: 1200px; overflow: hidden; background: var(--white); }
  body { position: relative; font-family: "Questrial", "Century Gothic", sans-serif; }

  .site-header { position: absolute; top: 0; left: 0; width: 1075px; height: 111px; }
  .brand { position: absolute; left: 103px; top: 38px; display: flex; align-items: center; gap: 10px;
           color: var(--green); font-size: 26px; }
  .brand-dot { width: 22px; height: 22px; border-radius: 50%; background: var(--green); }
  .main-nav a, .footer-nav a { position: absolute; text-decoration: none; white-space: nowrap; }
  .main-nav a { top: 55px; color: var(--nav-brown); font-size: 15px; }

  .hero { position: absolute; top: 111px; left: 0; width: 1075px; height: 447px;
          background: radial-gradient(ellipse at 75% 35%, #e6e79a 0%, transparent 45%),
                      linear-gradient(180deg, #d6d88f 0%, #b8c67a 45%, #7ea45a 100%); }
  .hero-band { position: absolute; top: 153px; left: 0; width: 100%; height: 138px; background: var(--band);
               text-align: center; color: var(--white); text-shadow: 1px 2px 3px rgba(0,0,0,0.35); }
  .hero-title { font-size: 43px; font-weight: 400; margin-top: 22px; letter-spacing: -0.3px; }
  .hero-sub { font-size: 20px; margin-top: 6px; }
  .hero-arrow { position: absolute; top: 201px; width: 41px; height: 41px; }

  .welcome-title, .services-title { position: absolute; left: 0; width: 1075px; text-align: center;
               color: var(--green); font-weight: 400; font-size: 30px; }
  .welcome-title { top: 580px; }
  .welcome-text { position: absolute; top: 638px; left: 114px; width: 842px; text-align: center;
               font-family: Arial, Helvetica, sans-serif; font-size: 12.5px; line-height: 21.5px; color: var(--body-text); }
  .read-more { position: absolute; top: 714px; left: 475px; width: 115px; height: 37px; border-radius: 4px;
               background: linear-gradient(var(--btn-top), var(--btn-bottom)); color: var(--white);
               font-family: Arial, Helvetica, sans-serif; font-size: 14px; line-height: 37px; text-align: center; }
  .services-title { top: 764px; }

  .service { position: absolute; top: 815px; width: 259px; }
  .service-photo { height: 139px; }
  .service h3 { font-weight: 400; font-size: 21.5px; color: var(--green); margin-top: 11px; }
  .service p { font-family: Arial, Helvetica, sans-serif; font-size: 12.5px; line-height: 21.5px;
               color: var(--body-text); margin-top: 4px; }

  .site-footer { position: absolute; top: 1058px; left: 0; width: 1075px; height: 142px; background: var(--brown); color: var(--white); }
  .footer-nav a { top: 22px; color: var(--white); font-size: 15px; }
  .social { position: absolute; top: 65px; left: 452px; display: flex; gap: 7px; }
  .social span { width: 29px; height: 29px; border-radius: 50%; background: linear-gradient(#f4f4f4, #cfcfcf); border: 1px solid #b9b9b9; }
  .copyright { position: absolute; top: 110px; left: 0; width: 1101px; text-align: center; font-size: 12.5px; }
</style>
</head>
<body>
  <header class="site-header">
    <div class="brand"><span class="brand-dot"></span>CalmHaven</div>
    <nav class="main-nav">
      <a href="#" style="left:394px">Home</a>
      <a href="#" style="left:464px">About us</a>
      <a href="#" style="left:553px">Services</a>
      <a href="#" style="left:637px">Patient Resources</a>
      <a href="#" style="left:785px">FAQ</a>
      <a href="#" style="left:843px">Contact us</a>
    </nav>
  </header>

  <section class="hero" role="img" aria-label="Soft-focus meadow of pale yellow wildflowers on green stems">
    <div class="hero-band">
      <h1 class="hero-title">We provides holistic psychiatry</h1>
      <p class="hero-sub">We focus on providing care to mothers and families.</p>
    </div>
    <svg class="hero-arrow" style="left:23px" viewBox="0 0 41 41"><circle cx="20.5" cy="20.5" r="20.5" fill="rgba(90,100,80,0.45)"/><path d="M23 13 L16 20.5 L23 28" stroke="#fff" stroke-width="3" fill="none"/></svg>
    <svg class="hero-arrow" style="left:1005px" viewBox="0 0 41 41"><circle cx="20.5" cy="20.5" r="20.5" fill="rgba(90,100,80,0.45)"/><path d="M18 13 L25 20.5 L18 28" stroke="#fff" stroke-width="3" fill="none"/></svg>
  </section>

  <h2 class="welcome-title">Welcome</h2>
  <p class="welcome-text">Sed ut perspiciatis unde omnis iste natus error sit voluptatem accusantium doloremque laudantium, totam rem aperiam, eaque ipsa quae ab illo inven-tore Nemo enim ipsam voluptatem quia voluptas sit aspernatur aut odit aut fugit, sed quia consequuntur magni dolores eos qui ratione voluptatem sequi nesciunt. Neque porro quisquam est, qui dolorem ipsum quia dolor sit amet,</p>
  <a class="read-more">Read More</a>

  <h2 class="services-title">Services</h2>
  <article class="service" style="left:110px">
    <div class="service-photo" role="img" aria-label="Woman in a cap relaxing among green trees" style="background:linear-gradient(135deg,#e3e8dc,#7da25a 60%,#4f7a34)"></div>
    <h3>for mothers</h3>
    <p>Sed ut perspiciatis unde omnis iste natus error sit voluptatem accusantium doloremque.</p>
  </article>
  <article class="service" style="left:408px">
    <div class="service-photo" role="img" aria-label="Smiling family of parents and two children together" style="background:linear-gradient(135deg,#8a8a88,#b5a596 55%,#6c6660)"></div>
    <h3>for families</h3>
    <p>Sed ut perspiciatis unde omnis iste natus error sit voluptatem accusantium doloremque.</p>
  </article>
  <article class="service" style="left:704px">
    <div class="service-photo" role="img" aria-label="Young woman jogging by the water at golden hour" style="background:linear-gradient(180deg,#c9a76a,#d8b873 55%,#8c7a38)"></div>
    <h3>for Youth</h3>
    <p>Sed ut perspiciatis unde omnis iste natus error sit voluptatem accusantium doloremque.</p>
  </article>

  <footer class="site-footer">
    <nav class="footer-nav">
      <a href="#" style="left:296px">Home</a>
      <a href="#" style="left:366px">About</a>
      <a href="#" style="left:437px">Services</a>
      <a href="#" style="left:521px">Patient Resources</a>
      <a href="#" style="left:668px">FAQ</a>
      <a href="#" style="left:726px">Contact</a>
    </nav>
    <div class="social" aria-label="Social links"><span></span><span></span><span></span><span></span><span></span></div>
    <p class="copyright">© 2014. www.calmhaven.example</p>
  </footer>
</body>
</html>
```